Web Developer Needs a Business Card Design

I need a personal business card design that represents me as a web developer for potential employers. I would like the background to be a dark color on the front for contrast with my logo and name. The back will have all my information along with a smaller version of the logo. I want something with a modern look and feel, not too conservative. This will be used for potential employers and freelance work.

Industry/Entity Type

Business

Contact Information for Business Card

Front should have my logo and name. The back should have all my personal information which would include: name: Tom Brevardi, phone: 570-614-9083, email: tombrevardi@mailwisp.com, website url: www.tombrevardi.com, logo, web developer.

Font styles to use
Sans Serif

Requirements
Must have
• Must include my logo. The color palette base color will be the logo color.

```html
<!DOCTYPE html>
<html lang="en">
<head>
<meta charset="utf-8">
<title>Tom Brevardi – Business Card</title>
<link href="https://fonts.googleapis.com/css2?family=Open+Sans:wght@300;400;600;700&display=swap" rel="stylesheet">
<style>
  :root {
    --stage: #dcd6cf;
    --card: #0b0b0b;
    --card-edge: #1c1c1c;
    --teal: #7fd3bf;
    --white: #ffffff;
    --muted: #e6e6e6;
  }
  * { margin: 0; padding: 0; box-sizing: border-box; }
  html, body {
    width: 1200px; height: 913px; overflow: hidden;
    background: var(--stage);
    font-family: "Open Sans", Arial, sans-serif;
  }
  .canvas { position: relative; width: 1200px; height: 913px; }

  .card {
    position: absolute;
    width: 580px; height: 330px;
    background: linear-gradient(135deg, var(--card-edge) 0%, var(--card) 55%);
    border-radius: 18px;
    overflow: hidden;
    box-shadow: 0 14px 30px rgba(0,0,0,.28);
  }
  .card--back { left: 70px; top: 90px; }
  .card--front { left: 550px; top: 490px; }

  /* back side */
  .divider {
    position: absolute; left: 0; right: 0; top: 128px;
    height: 2px; background: var(--white);
  }
  .divider--short {
    top: 232px; right: auto; width: 40px; height: 2px;
  }
  .logo-mark {
    position: absolute;
    width: 136px; height: 136px;
    border: 9px solid var(--teal);
    border-radius: 50%;
    background: var(--card);
    display: flex; align-items: center; justify-content: center;
    color: var(--teal);
    font-weight: 700; font-size: 19px; letter-spacing: .5px;
  }
  .card--back .logo-mark { left: 370px; top: 60px; }

  .identity { position: absolute; left: 40px; top: 66px; }
  .identity__name {
    color: var(--white); font-weight: 700; font-size: 24px;
    letter-spacing: .5px; text-transform: uppercase; line-height: 1.1;
  }
  .identity__role {
    color: var(--teal); font-weight: 600; font-size: 15px;
    letter-spacing: 1px; text-transform: uppercase;
  }

  .contact { position: absolute; left: 56px; top: 154px; list-style: none; }
  .contact li {
    display: flex; align-items: center; gap: 9px;
    color: var(--muted); font-size: 15px; line-height: 23px;
  }
  .contact svg { width: 13px; height: 13px; flex: none; }

  .swoosh { position: absolute; left: 0; bottom: 0; width: 580px; height: 180px; }

  /* front side */
  .card--front .logo-mark { left: 222px; top: 42px; }
  .headline {
    position: absolute; left: 0; right: 0; top: 200px;
    text-align: center;
  }
  .headline__name {
    color: var(--white); font-weight: 400; font-size: 34px;
    letter-spacing: 2px; text-transform: uppercase;
  }
  .headline__role {
    color: var(--muted); font-weight: 400; font-size: 18px;
    letter-spacing: .5px; margin-top: 4px;
  }
</style>
</head>
<body>
<main class="canvas">

  <section class="card card--back" aria-label="Card back with contact details">
    <div class="divider"></div>
    <div class="divider divider--short"></div>
    <div class="logo-mark">Brevardi</div>

    <div class="identity">
      <p class="identity__name">Tom Brevardi</p>
      <p class="identity__role">Web Developer</p>
    </div>

    <ul class="contact">
      <li>
        <svg viewBox="0 0 24 24" fill="var(--teal)"><path d="M6.6 10.8a15 15 0 0 0 6.6 6.6l2.2-2.2c.3-.3.7-.4 1-.2 1.1.4 2.3.6 3.6.6.6 0 1 .4 1 1V20c0 .6-.4 1-1 1A17 17 0 0 1 3 4c0-.6.4-1 1-1h3.5c.6 0 1 .4 1 1 0 1.3.2 2.5.6 3.6.1.3 0 .7-.2 1z"/></svg>
        570-614-9083
      </li>
      <li>
        <svg viewBox="0 0 24 24" fill="none" stroke="var(--teal)" stroke-width="2.4"><rect x="2" y="5" width="20" height="14" rx="2"/><path d="M2 6l10 7 10-7"/></svg>
        tombrevardi@mailwisp.com
      </li>
      <li>
        <svg viewBox="0 0 24 24" fill="none" stroke="var(--teal)" stroke-width="2.2"><circle cx="12" cy="12" r="10"/><path d="M2 12h20M12 2c3 3 3 17 0 20M12 2c-3 3-3 17 0 20"/></svg>
        www.tombrevardi.com
      </li>
    </ul>

    <svg class="swoosh" viewBox="0 0 580 180" preserveAspectRatio="none" aria-hidden="true">
      <path d="M0 150 C160 95 380 60 580 0 L580 180 L0 180 Z" fill="var(--white)"/>
      <path d="M0 168 C170 118 390 80 580 24 L580 180 L0 180 Z" fill="var(--teal)"/>
    </svg>
  </section>

  <section class="card card--front" aria-label="Card front with name">
    <div class="logo-mark">Brevardi</div>
    <div class="headline">
      <p class="headline__name">Tom Brevardi</p>
      <p class="headline__role">Front-End Developer</p>
    </div>
  </section>

</main>
</body>
</html>
```